Jewelers Website

This is for the DESIGN ONLY.
I am a software programmer and will be doing the development.
New website design for
www.lunagemcraft.com.au
Need a fresh new look for an online only jewellery business who produce their jewellery by hand. I would like it designed in a parallax style. Feel free to recommend fonts to use for the site. This is an Australian based company located in NSW so shots of sites in NSW might make nice background images.
http://plaxorin.me/demo/#theme=parallax
To contain the below sections
About Us
Contact Us
Gallery
Testimonials
Diamond Types
The colour scheme is to be Black / White and Silver.
With the Parallax style there will be moving sections and images for added impact.
Target Market(s)
Young Adults mainly engagement jewellery

```html
<!DOCTYPE html>
<html lang="en">
<head>
<meta charset="utf-8">
<title>Luna Gemcraft</title>
<link href="https://fonts.googleapis.com/css2?family=Lato:wght@300;400;700&display=swap" rel="stylesheet">
<style>
:root{
  --ink:#111;
  --white:#fff;
  --footer:#1c1c1c;
  --footer-line:#4a4a4a;
  --grey-text:#555;
  --soft-grey:#f4f4f4;
  --silver:#cfcfcf;
  --muted:#c8c8c8;
}
*{box-sizing:border-box;margin:0;padding:0}
html,body{width:1115px;height:1200px;overflow:hidden;background:var(--white);font-family:'Lato',sans-serif}
.page{position:relative;width:1115px;height:1200px}
.hero{position:absolute;left:0;top:0;width:1115px;height:411px;
  background:radial-gradient(ellipse at 50% 55%,#9a9a9a 0%,#5c5c5c 35%,#2a2a2a 70%,#141414 100%)}
.brand{position:absolute;left:93px;top:52px;width:152px;height:54px;background:#2b2b2b;border:1px solid #555;
  color:var(--white);font-weight:400;font-size:21px;line-height:22px;text-align:center;padding-top:5px;letter-spacing:1px}
.main-nav{position:absolute;top:50px;left:380px;right:88px;display:flex;justify-content:space-between}
.main-nav a{color:var(--white);font-size:12px;font-weight:700;text-decoration:none;letter-spacing:.2px}
.slider-dots{position:absolute;top:365px;left:515px;display:flex;gap:6px}
.slider-dots span{width:24px;height:21px;border-radius:50%;background:var(--white)}
.slider-dots span.active{background:var(--ink);border:4px solid var(--white)}
.welcome{position:absolute;left:90px;top:404px;width:936px;height:162px;
  background:linear-gradient(#fff,#f3f3f3);box-shadow:0 8px 10px -8px rgba(0,0,0,.2);text-align:center}
.welcome h1{position:relative;margin-top:25px;font-size:25px;font-weight:700;color:var(--ink);letter-spacing:.3px}
.welcome h1 span{background:#fff;padding:0 6px;position:relative}
.welcome h1:before{content:"";position:absolute;left:26px;right:26px;top:50%;border-top:1px solid #ccc}
.welcome p{margin:10px auto 0;width:830px;font-size:13.5px;line-height:15px;color:var(--grey-text)}
.btn-read{display:inline-block;margin-top:10px;width:118px;height:30px;line-height:30px;font-size:13px;color:#999;
  background:linear-gradient(135deg,#eee 50%,#e2e2e2 50%)}
.features{position:absolute;top:588px;left:0;width:1115px}
.feature{position:absolute;width:240px;text-align:center}
.feature .icon{margin:0 auto;width:90px;height:76px;border-radius:50%;background:var(--soft-grey);display:flex;align-items:center;justify-content:center}
.feature .icon.dark{background:var(--ink)}
.feature h2{margin-top:15px;font-size:15.5px;font-weight:700;color:var(--ink)}
.feature p{margin-top:6px;font-size:11px;line-height:13px;color:#777}
.feature .btn-small{display:inline-block;margin-top:8px;width:85px;height:22px;line-height:22px;font-size:9px;color:#ccc;background:#f6f6f6}
.footer{position:absolute;left:0;top:843px;width:1115px;height:357px;background:var(--footer);border-top:2px solid #888;color:var(--white)}
.footer h3{position:absolute;top:35px;font-size:24px;font-weight:300}
.foot-nav{position:absolute;left:82px;top:85px;list-style:none}
.foot-nav li{font-size:15.5px;font-weight:300;margin-bottom:15px}
.legal{position:absolute;left:111px;top:255px;font-size:9.5px;font-family:Arial,sans-serif}
.address{position:absolute;left:312px;top:85px;font-size:15.5px;font-weight:300;line-height:19px}
.phones{position:absolute;left:312px;top:170px;font-size:15.5px;font-weight:300;line-height:24px}
.addr-icon{position:absolute;left:286px}
.socials{position:absolute;left:313px;top:240px;display:flex;gap:12px}
.socials span{width:20px;height:20px;border-radius:50%;background:var(--white)}
.field{position:absolute;border:2px solid var(--white);border-radius:8px;font-size:15.5px;font-weight:300;padding:10px 11px}
.submit{position:absolute;left:915px;top:231px;width:117px;height:31px;border-radius:5px;background:var(--silver);
  color:var(--white);font-size:14px;text-align:center;line-height:31px}
.footer-rule{position:absolute;left:0;right:0;top:292px;border-top:1px solid var(--footer-line)}
.copyright{position:absolute;left:82px;top:318px;font-size:11.5px;font-family:Arial,sans-serif}
</style>
</head>
<body>
<div class="page">
  <header class="hero" role="img" aria-label="Photograph of loose round brilliant diamonds on dark fabric">
    <div class="brand">LUNA<br>GEMCRAFT</div>
    <nav class="main-nav">
      <a href="#">HOME</a><a href="#">ABOUT US</a><a href="#">GALLERY</a><a href="#">TESTIMONIALS</a><a href="#">DIAMOND TYPES</a><a href="#">CONTACT US</a>
    </nav>
    <div class="slider-dots"><span></span><span class="active"></span><span></span></div>
  </header>

  <section class="welcome">
    <h1><span>WELCOME TO LUNA GEMCRAFT</span></h1>
    <p>Lorem ipsum dolor sit amet, consectetur adipisicing elit, sed do eiusmod tempor incididunt ut labore et dolore magna aliqua. Ut enim ad minim veniam, quis nostrud exercitation ullamco laboris nisi ut aliquip ex ea commodo consequat. Duis aute irure dolor in reprehenderit in voluptate velit esse</p>
    <span class="btn-read">Read More</span>
  </section>

  <section class="features">
    <div class="feature" style="left:87px">
      <div class="icon dark"><svg width="40" height="40" viewBox="0 0 40 40"><circle cx="20" cy="20" r="19" fill="#fff"/><circle cx="21" cy="11" r="3" fill="#111"/><path d="M16 17h7l-3 13h3v2h-8l3-13h-2z" fill="#111"/></svg></div>
      <h2>ABOUT US</h2>
      <p>Lorem ipsum dolor sit amet, consectetur adipisicing elit, sed do eiusmod tempor incididunt ut labore et</p>
      <span class="btn-small">Read More</span>
    </div>
    <div class="feature" style="left:437px">
      <div class="icon"><svg width="48" height="40" viewBox="0 0 48 40"><g fill="#bbb"><circle cx="18" cy="25" r="9"/><circle cx="32" cy="13" r="7"/></g><g fill="#f4f4f4"><circle cx="18" cy="25" r="3.5"/><circle cx="32" cy="13" r="2.5"/></g><g stroke="#bbb" stroke-width="4"><path d="M18 13v24M6 25h24M10 17l16 16M26 17l-16 16"/><path d="M32 4v18M23 13h18M26 7l12 12M38 7l-12 12"/></g><circle cx="18" cy="25" r="3.5" fill="#f4f4f4"/><circle cx="32" cy="13" r="2.5" fill="#f4f4f4"/></svg></div>
      <h2>OUR SERVICES</h2>
      <p>Lorem ipsum dolor sit amet, consectetur adipisicing elit, sed do eiusmod tempor incididunt ut labore et</p>
      <span class="btn-small">Read More</span>
    </div>
    <div class="feature" style="left:774px">
      <div class="icon"><svg width="60" height="30" viewBox="0 0 60 30"><rect x="4" y="5" width="26" height="20" rx="3" fill="#bbb"/><path d="M6 8l11 9 11-9" stroke="#eee" stroke-width="2" fill="none"/><rect x="35" y="5" width="21" height="21" rx="3" fill="#bbb"/></svg></div>
      <h2>CONNECT WITH US</h2>
      <p>Lorem ipsum dolor sit amet, consectetur adipisicing elit, sed do eiusmod tempor incididunt ut labore et</p>
      <span class="btn-small">Read More</span>
    </div>
  </section>

  <footer class="footer">
    <h3 style="left:80px">Navigation</h3>
    <h3 style="left:290px">Address</h3>
    <h3 style="left:629px">Contact Us</h3>
    <ul class="foot-nav"><li>Home</li><li>About Us</li><li>Properties</li><li>Contact Us</li></ul>
    <div class="legal">Copyright@2014 PRIVACY POLICY</div>
    <svg class="addr-icon" style="top:88px" width="14" height="14" viewBox="0 0 14 14"><path d="M13 1L1 6l6 1 1 6z" fill="#fff"/></svg>
    <div class="address">Sydney<br>Kelloway NSW 2209, Australia<br>Germany<br>41920 Brevenau, Germany</div>
    <svg class="addr-icon" style="top:174px" width="14" height="15" viewBox="0 0 14 15"><path d="M3 1l3 3-2 2c1 2 3 4 5 5l2-2 3 3-2 2C6 14 0 8 1 3z" fill="#fff"/></svg>
    <div class="phones">+61 (0)2 9000 4821<br>+49 (0)2153 0004720</div>
    <div class="socials"><span></span><span></span><span></span><span></span></div>
    <div class="field" style="left:631px;top:78px;width:157px;height:42px">Name</div>
    <div class="field" style="left:807px;top:78px;width:225px;height:42px">Email</div>
    <div class="field" style="left:631px;top:136px;width:401px;height:79px">Message</div>
    <div class="submit">Submit</div>
    <div class="footer-rule"></div>
    <div class="copyright">© Copyright 2002-2012 Luna Gemcraft Pty Ltd(ABN 12 345 678 901)</div>
  </footer>
</div>
</body>
</html>
```